K.Wren Customer Retention Business Infographic

I am looking to create an infographic by transforming the following data to be used on my website and proposals. I have specific colors that I would like to blend with and a concept of what it could look like, but open. I want to be able to show the comparison...of the two data points side by side.

Target Market(s)

Passionate Business owners

Industry/Entity Type

Business consulting

Font styles to use
Sans Serif

Requirements
Must have
• Concise infographic side by side comparision to use on website and proposals

```html
<!DOCTYPE html>
<html lang="en">
<head>
<meta charset="utf-8">
<title>Customer Retention Infographic</title>
<link rel="stylesheet" href="https://fonts.googleapis.com/css2?family=Source+Sans+3:wght@400;600;700;800&display=swap">
<style>
  :root {
    --navy: #1d2a5b;
    --slate: #5a6c9c;
    --orange: #f3a24b;
    --paper: #f7f8fb;
    --brace: #c3c4c6;
    --white: #ffffff;
  }
  * { margin: 0; padding: 0; box-sizing: border-box; }
  html, body { width: 1200px; height: 763px; overflow: hidden; }
  body {
    background: var(--paper);
    font-family: "Source Sans 3", Arial, sans-serif;
    position: relative;
  }
  .infographic { position: absolute; inset: 0; }
  .band { position: absolute; left: 0; width: 100%; background: var(--navy); }
  .band--top { top: 28px; height: 13px; }
  .band--bottom { bottom: 0; height: 16px; }
  .title-tab { position: absolute; left: 132px; top: 40px; width: 910px; height: 48px; }
  .title {
    position: absolute; left: 132px; top: 40px; width: 910px; height: 48px;
    display: flex; align-items: center; justify-content: center;
    color: var(--white); font-weight: 800; font-size: 34px; letter-spacing: 0.2px;
  }
  .intro {
    position: absolute; top: 118px; width: 460px;
    color: var(--navy); font-weight: 700; font-size: 21px; line-height: 1.25;
    text-align: center;
  }
  .intro--gain { left: 17px; }
  .intro--cost { left: 724px; }
  .icon { position: absolute; }
  .icon--clipboard { left: 222px; top: 238px; width: 58px; height: 62px; }
  .icon--person {
    left: 930px; top: 232px; width: 54px; height: 72px;
    background: linear-gradient(180deg, #fbe2c4, #f6c58d); border-radius: 6px;
  }
  .column-heading {
    position: absolute; top: 318px; width: 460px; text-align: center;
    font-weight: 700; font-size: 23px; letter-spacing: 0.3px;
  }
  .column-heading--gain { left: 17px; color: var(--slate); }
  .column-heading--cost { left: 724px; color: var(--orange); }
  .facts { position: absolute; list-style: none; font-size: 18px; line-height: 1.3; }
  .facts--gain { left: 42px; top: 384px; width: 400px; color: var(--slate); }
  .facts--cost { left: 758px; top: 384px; width: 390px; color: var(--orange); }
  .facts li { position: relative; padding-left: 28px; margin-bottom: 23px; }
  .facts li svg { position: absolute; left: 0; top: 5px; width: 16px; height: 13px; }
  .facts strong { font-weight: 700; }
  .brace { position: absolute; top: 268px; width: 42px; height: 420px; }
  .brace--left { left: 466px; }
  .brace--right { left: 694px; }
  .gap-arrow { position: absolute; left: 584px; top: 312px; width: 36px; height: 102px; }
  .gap-label {
    position: absolute; left: 530px; top: 440px; width: 144px; text-align: center;
    color: var(--navy); font-weight: 700; font-size: 31px; line-height: 1.1;
  }
</style>
</head>
<body>
<main class="infographic">
  <div class="band band--top"></div>
  <svg class="title-tab" viewBox="0 0 910 48" preserveAspectRatio="none" aria-hidden="true">
    <path d="M0 0 H910 C885 4 878 48 850 48 H60 C32 48 25 4 0 0 Z" fill="#1d2a5b"/>
  </svg>
  <h1 class="title">WHEN CUSTOMERS ENGAGE BUSINESSES FLOURISH</h1>

  <p class="intro intro--gain">When your customers are happy and your business becomes an essential part of their lives… you experience</p>
  <p class="intro intro--cost">When your customers are not ecstatic, you are stuck with stagnant growth and dropping retention rate … it costs you</p>

  <svg class="icon icon--clipboard" viewBox="0 0 58 62" aria-hidden="true" fill="none" stroke="#5a6c9c" stroke-width="2.4">
    <rect x="4" y="7" width="40" height="52" rx="3"/>
    <rect x="15" y="2" width="18" height="9" rx="2"/>
    <line x1="11" y1="20" x2="17" y2="20"/><line x1="11" y1="27" x2="17" y2="27"/>
    <line x1="11" y1="34" x2="17" y2="34"/><line x1="11" y1="41" x2="17" y2="41"/>
    <line x1="11" y1="48" x2="17" y2="48"/>
    <circle cx="42" cy="32" r="12" stroke="#f3a24b"/>
    <path d="M36 32 l4 4 l8 -8" stroke="#f3a24b"/>
  </svg>
  <div class="icon icon--person" role="img" aria-label="Outline icon of a customer service agent"></div>

  <h2 class="column-heading column-heading--gain">EMPLOYER BENEFITS</h2>
  <h2 class="column-heading column-heading--cost">EMPLOYEE NEEDS</h2>

  <ul class="facts facts--gain">
    <li><svg viewBox="0 0 16 13"><path d="M1 7 l5 4 l9 -10" fill="none" stroke="#5a6c9c" stroke-width="2.4"/></svg>Boost profits by <strong>25% to 95%</strong> with <strong>5% increase</strong> in customer retention</li>
    <li><svg viewBox="0 0 16 13"><path d="M1 7 l5 4 l9 -10" fill="none" stroke="#5a6c9c" stroke-width="2.4"/></svg><strong>65%</strong> of your business comes from repeat customers.</li>
    <li><svg viewBox="0 0 16 13"><path d="M1 7 l5 4 l9 -10" fill="none" stroke="#5a6c9c" stroke-width="2.4"/></svg><strong>60%</strong> of loyal customers will talk about YOU with their friends and family.</li>
    <li><svg viewBox="0 0 16 13"><path d="M1 7 l5 4 l9 -10" fill="none" stroke="#5a6c9c" stroke-width="2.4"/></svg><strong>60-70%</strong> probability of selling to an existing customer</li>
  </ul>

  <svg class="brace brace--left" viewBox="0 0 42 420" preserveAspectRatio="none" aria-hidden="true">
    <path d="M4 4 C30 10 24 60 24 120 C24 170 26 200 38 210 C26 220 24 250 24 300 C24 360 30 410 4 416" fill="none" stroke="#c3c4c6" stroke-width="6" stroke-linecap="round"/>
  </svg>
  <svg class="gap-arrow" viewBox="0 0 36 102" aria-hidden="true">
    <line x1="18" y1="0" x2="18" y2="98" stroke="#1d2a5b" stroke-width="2.6"/>
    <path d="M3 82 L18 99 L33 82" fill="none" stroke="#1d2a5b" stroke-width="2.6"/>
  </svg>
  <p class="gap-label">The<br>Gap</p>
  <svg class="brace brace--right" viewBox="0 0 42 420" preserveAspectRatio="none" aria-hidden="true">
    <path d="M38 4 C12 10 18 60 18 120 C18 170 16 200 4 210 C16 220 18 250 18 300 C18 360 12 410 38 416" fill="none" stroke="#c3c4c6" stroke-width="6" stroke-linecap="round"/>
  </svg>

  <ul class="facts facts--cost">
    <li><svg viewBox="0 0 16 13"><path d="M1 7 l5 4 l9 -10" fill="none" stroke="#f3a24b" stroke-width="2.4"/></svg><strong>5x</strong> higher cost to acquire new customers than retain existing ones</li>
    <li><svg viewBox="0 0 16 13"><path d="M1 7 l5 4 l9 -10" fill="none" stroke="#f3a24b" stroke-width="2.4"/></svg>Costs <strong>16 times</strong> more to build a long-term relationship with a new customer.</li>
    <li><svg viewBox="0 0 16 13"><path d="M1 7 l5 4 l9 -10" fill="none" stroke="#f3a24b" stroke-width="2.4"/></svg><strong>5% to 20%</strong> probability of selling to a new prospect</li>
  </ul>

  <div class="band band--bottom"></div>
</main>
</body>
</html>
```